依頼詳細
■地域系LP(PC・スマホサイト)
ページ数:各1ページづつ作成
ワイヤーフレーム:あり
https://pelvix.com/diagrams/RaqM8WbNpe4kV2sY#913KD

※メイン画像部分は写真を入れ込んでデザインお願いします。
(それ以外の素材は支給頂ける予定)
※有料画像を使用する場合は画像の費用は自己負担でお願いします。
※PC、スマホ版ともにデザインの方向性は合わせてください。
※スマホ版は幅640pxで作成お願いします。

■デザイン参考サイト
https://mosuplint.jp/
https://mosuplint.jp/lp/sp/300aa/00/00/00/

■コーディング
一切不要。

■ページ数
PC1ページ
スマホ1ページ
■納品
画像データと制作ファイルを納品ください。
(それ以外の素材は支給頂ける予定)
※スマホ版は幅640pxで作成お願いします。
■ 選んだ理由

情報の伝わりやすいさ、すっきりとしたデザインを評価させていただきました。

■ 提案者全員のお礼・コメント

ご応募くださり、ありがとうございます。
また次回のデザインコンペにもご参加いただけますと幸いです。
よろしくお願いいたします。

```html
<!DOCTYPE html>
<html lang="ja">
<head>
<meta charset="utf-8">
<title>モスプリント | 東京都で正社員へ</title>
<link rel="stylesheet" href="https://fonts.googleapis.com/css2?family=Noto+Sans+JP:wght@400;500;700;900&display=swap">
<style>
:root{
  --green:#8cc220;
  --green-dark:#6fa30f;
  --green-pale:#eef6dc;
  --ink:#333333;
  --ink-soft:#666666;
  --charcoal:#3b3b3b;
  --charcoal-deep:#2b2b2b;
  --yellow:#f6d800;
  --gray-bg:#efefef;
  --line:#d9d9d9;
  --red:#d9362b;
  --white:#ffffff;
}
*{box-sizing:border-box;margin:0;padding:0}
html,body{width:1200px;height:3672px;overflow:hidden}
body{font-family:"Noto Sans JP",sans-serif;color:var(--ink);background:var(--white);position:relative}
.abs{position:absolute}

/* hero */
.hero{position:absolute;left:0;top:0;width:1200px;height:600px;background:linear-gradient(180deg,#ffffff 0%,#f4f9ea 70%,#e7f2d0 100%);overflow:hidden}
.brand{position:absolute;left:30px;top:20px;display:flex;align-items:center;gap:10px;font-size:30px;font-weight:900;color:var(--green)}
.brand-mark{width:22px;height:22px;background:var(--green)}
.hero-people{position:absolute;left:640px;top:0;width:560px;height:480px;background:linear-gradient(160deg,#dfe6d5,#c8cfc2 60%,#b7bcb4)}
.hero-eyebrow{position:absolute;left:30px;top:130px;font-size:26px;font-weight:700;color:var(--ink)}
.hero-eyebrow b{background:var(--green);color:#fff;padding:2px 10px;margin-right:4px}
.hero-line1{position:absolute;left:30px;top:178px;font-size:56px;font-weight:900;letter-spacing:-1px}
.hero-line1 em{font-style:normal;color:var(--green);font-size:70px}
.hero-line2{position:absolute;left:30px;top:260px;font-size:66px;font-weight:900;color:var(--green-dark);letter-spacing:-1px}
.hero-line2 .from{display:inline-block;background:var(--green);color:#fff;font-size:30px;padding:4px 8px;vertical-align:middle;margin:0 6px;border-radius:4px}
.stats{position:absolute;left:24px;top:380px;display:flex;gap:8px}
.stat{width:220px;height:88px;background:#fff;border:2px solid var(--green)}
.stat-label{background:var(--green);color:#fff;font-size:15px;font-weight:700;text-align:center;height:30px;line-height:30px}
.stat-value{text-align:center;font-size:36px;font-weight:900;color:var(--ink);line-height:54px}
.stat-value small{font-size:18px}
.stat-note{position:absolute;left:24px;top:474px;font-size:11px;color:var(--ink-soft)}
.hero-support{position:absolute;left:24px;top:500px;font-size:28px;font-weight:900;line-height:1.35;color:var(--ink)}
.hero-support span{color:var(--green-dark)}
.consultant{position:absolute;left:660px;top:488px;width:190px;height:100px;background:linear-gradient(180deg,#d8d8d8,#bcbcbc)}
.venue{position:absolute;left:930px;top:420px;width:220px;height:220px;border-radius:50%;border:6px solid #fff;background:linear-gradient(180deg,#c9dceb,#9fb3c3)}
.venue-tag{position:absolute;left:940px;top:600px;width:200px;background:var(--green);color:#fff;font-size:14px;font-weight:700;text-align:center;padding:4px 0;line-height:1.3;z-index:2}

/* cta band */
.cta-band{position:absolute;left:0;top:600px;width:1200px;height:110px;background:var(--charcoal);display:flex;align-items:center;padding:0 30px;gap:40px}
.cta-lead{color:#fff;font-size:20px;font-weight:700;line-height:1.4;width:220px}
.cta-button{width:380px;height:74px;background:var(--yellow);border-radius:6px;display:flex;align-items:center;justify-content:center;gap:14px;font-size:22px;font-weight:900;color:var(--ink);line-height:1.3;box-shadow:0 4px 0 #b89f00}
.cta-phone{color:#fff;margin-left:20px}
.cta-phone .label{font-size:16px;font-weight:700}
.cta-phone .num{display:flex;align-items:center;gap:10px;font-size:42px;font-weight:900;color:var(--yellow);line-height:1.1}
.cta-phone .hours{font-size:12px;color:#ccc}

/* rate */
.rate{position:absolute;left:0;top:710px;width:1200px;height:250px;background:#fff;text-align:center}
.rate-title{position:absolute;left:240px;top:50px;width:720px;font-size:44px;font-weight:900;line-height:1.35}
.rate-title em{font-style:normal;color:var(--green-dark)}
.rate-brace{position:absolute;top:50px;width:40px;height:110px;border:6px solid var(--green)}
.rate-brace.l{left:200px;border-right:none}
.rate-brace.r{right:200px;border-left:none}
.rate-so{position:absolute;left:0;top:200px;width:1200px;font-size:22px;font-weight:700}

/* voices */
.voices{position:absolute;left:0;top:960px;width:1200px;height:800px;background:var(--gray-bg)}
.voices-arrow{position:absolute;left:570px;top:0}
.voices-head{position:absolute;left:240px;top:40px;width:720px;height:120px;background:var(--green);color:#fff;text-align:center;font-size:30px;font-weight:900;line-height:1.4;padding-top:20px}
.voices-head span{color:var(--yellow)}
.voice{position:absolute;top:220px;width:555px;height:540px;background:#fff;padding:30px}
.voice.a{left:30px}.voice.b{left:615px}
.voice-name{font-size:32px;font-weight:700}
.voice-name small{font-size:16px;font-weight:400;margin-left:8px}
.voice-tags{margin-top:10px;display:flex;align-items:center;gap:8px;font-size:14px;font-weight:700}
.tag{padding:3px 10px;border:2px solid var(--green);color:var(--green-dark)}
.tag.after{background:var(--green);color:#fff}
.voice-photo{position:absolute;right:30px;top:26px;width:130px;height:130px;border-radius:50%;background:linear-gradient(180deg,#e2e2e2,#bdbdbd)}
.voice-body{margin-top:80px;font-size:15px;line-height:1.85;color:var(--ink-soft)}

/* form */
.apply{position:absolute;left:0;top:1760px;width:1200px;height:1360px;background:#fff}
.apply-box{position:absolute;left:30px;top:70px;width:1140px;height:1250px;border:1px solid var(--line)}
.apply-head{height:64px;background:var(--green);color:#fff;font-size:24px;font-weight:900;line-height:64px;padding-left:30px}
.apply-intro{padding:26px 60px 16px;font-size:13px;line-height:1.8;color:var(--ink-soft)}
.form-table{margin:0 60px;border-top:1px solid var(--line)}
.row{display:flex;border-bottom:1px solid var(--line);min-height:62px}
.row-label{width:260px;background:#f6f6f6;display:flex;align-items:center;justify-content:space-between;padding:0 16px;font-size:16px;font-weight:700}
.req{background:var(--red);color:#fff;font-size:11px;padding:2px 8px;border-radius:2px}
.row-field{flex:1;display:flex;align-items:center;gap:14px;padding:0 20px;font-size:14px;color:var(--ink-soft)}
.input{height:34px;border:1px solid #bbb;background:#fff}
.select{height:34px;border:1px solid #bbb;background:#fff;width:160px;padding-left:10px;line-height:32px;color:var(--ink)}
.radio{display:inline-flex;align-items:center;gap:6px}
.radio i{width:14px;height:14px;border:1px solid #999;border-radius:50%;display:inline-block}
.radio i.on{background:radial-gradient(circle,#555 40%,#fff 45%)}
.row.tall{min-height:150px}
.agree{margin:40px 60px 0;border:1px solid var(--line);padding:20px;text-align:center;font-size:15px}
.agree a{color:#1d6fc2}
.agree p{font-size:12px;color:var(--ink-soft);margin-top:8px}
.submit{margin:40px auto 0;width:440px;height:76px;background:var(--green);border-radius:8px;color:#fff;font-size:26px;font-weight:900;text-align:center;line-height:76px;box-shadow:0 5px 0 var(--green-dark)}

/* access */
.access{position:absolute;left:0;top:3120px;width:1200px;height:420px;background:var(--charcoal-deep);color:#fff}
.access-title{position:absolute;left:40px;top:36px;font-size:26px;font-weight:900}
.access-text{position:absolute;left:40px;top:90px;width:360px;font-size:14px;line-height:1.9;color:#ddd}
.office{position:absolute;top:30px;width:330px}
.office.main{left:460px}.office.branch{left:820px}
.office-name{font-size:20px;font-weight:700;text-align:center;margin-bottom:10px}
.office-photo{height:220px;background:linear-gradient(180deg,#8fa6b8,#5e6f7c)}
.office-addr{font-size:13px;line-height:1.6;margin-top:10px;color:#ddd}
.pagetop{position:absolute;right:30px;top:380px;background:var(--green);color:#fff;font-size:14px;padding:8px 18px}

.foot{position:absolute;left:0;top:3540px;width:1200px;height:132px;background:#fff;border-top:6px solid var(--green)}
.foot-badge{position:absolute;left:40px;top:30px;width:64px;height:64px;border-radius:50%;background:#e2e2e2}
.copy{position:absolute;left:0;top:52px;width:1200px;text-align:center;font-size:14px;color:var(--ink-soft)}
</style>
</head>
<body>

<section class="hero">
  <div class="hero-people" role="img" aria-label="笑顔でガッツポーズをするスーツ姿の男女の写真"></div>
  <div class="brand"><span class="brand-mark"></span>モスプリント</div>
  <p class="hero-eyebrow"><b>東京都</b>で正社員求人をお探しの</p>
  <p class="hero-line1"><em>20代</em>のフリーター、既卒、</p>
  <p class="hero-line2">未経験<span class="from">から</span>正社員へ!</p>
  <div class="stats">
    <div class="stat"><div class="stat-label">サービス利用者</div><div class="stat-value">34,042<small>人</small></div></div>
    <div class="stat"><div class="stat-label">未経験OKの求人案件</div><div class="stat-value">1,000<small>件以上</small></div></div>
    <div class="stat"><div class="stat-label">内定率</div><div class="stat-value">78.7<small>%</small></div></div>
  </div>
  <p class="stat-note">※2014年3月時点</p>
  <p class="hero-support"><span>あなた専属のコンサルタント</span>が<br>東京都での就職活動を徹底サポート!</p>
  <div class="consultant" role="img" aria-label="面談をするコンサルタントの写真"></div>
  <div class="venue" role="img" aria-label="渋谷のオフィスビル外観の写真"></div>
  <div class="venue-tag">渋谷ミナモタワーで<br>無料カウンセリング</div>
</section>

<section class="cta-band">
  <p class="cta-lead">東京都で<br>就職カウンセリングを<br>受けるなら</p>
  <div class="cta-button">
    <svg width="38" height="28" viewBox="0 0 38 28"><rect x="1" y="1" width="36" height="26" fill="#fff" stroke="#333" stroke-width="2"/><path d="M1 1 L19 16 L37 1" fill="none" stroke="#333" stroke-width="2"/></svg>
    <span>無料カウンセリング<br>お申し込みはコチラ</span>
  </div>
  <div class="cta-phone">
    <p class="label">お電話でのお問い合わせ</p>
    <p class="num"><svg width="42" height="30" viewBox="0 0 42 30"><rect width="42" height="30" rx="4" fill="#f6d800"/><circle cx="13" cy="15" r="7" fill="none" stroke="#3b3b3b" stroke-width="3"/><circle cx="29" cy="15" r="7" fill="none" stroke="#3b3b3b" stroke-width="3"/></svg>0120-486-273</p>
    <p class="hours">年中無休24時間いつでも対応</p>
  </div>
</section>

<section class="rate">
  <div class="rate-brace l"></div><div class="rate-brace r"></div>
  <h2 class="rate-title">「モスプリント」なら<br>就職内定率<em>78%以上!</em></h2>
  <p class="rate-so">だから</p>
</section>

<section class="voices">
  <svg class="voices-arrow" width="60" height="30" viewBox="0 0 60 30"><path d="M0 0 H60 L30 30Z" fill="#fff"/></svg>
  <h2 class="voices-head">「<span>モスプリント</span>」を利用して就職された方から<br>多くの満足の声をいただいております!</h2>
  <article class="voice a">
    <p class="voice-name">M.Sさん<small>女性(23歳)</small></p>
    <p class="voice-tags"><span class="tag">時給900円</span>▶<span class="tag after">月給23万</span></p>
    <div class="voice-photo" role="img" aria-label="利用者女性の写真"></div>
    <p class="voice-body">高校を卒業してからアルバイトを続けていましたが、将来への不安から正社員を目指すことにしました。何から始めればよいか分からない状態でしたが、担当の方が私の希望を丁寧に聞いてくれ、自分に合う求人を一緒に探してくれました。<br><br>面接の前には練習の時間を作っていただき、話し方や服装まで具体的に教わりました。おかげで自信を持って面接に臨むことができ、希望していた事務職で内定をいただけました。今は毎日充実した気持ちで働いています。</p>
  </article>
  <article class="voice b">
    <p class="voice-name">S.Iさん<small>男性(25歳)</small></p>
    <p class="voice-tags"><span class="tag">時給1,000円</span>▶<span class="tag after">月給27万</span></p>
    <div class="voice-photo" role="img" aria-label="利用者男性の写真"></div>
    <p class="voice-body">大学を中退してから数年間、飲食店のアルバイトをしながらフリーター生活を送っていました。正社員経験がないことに引け目を感じていましたが、コンサルタントの方が強みを一緒に見つけてくれました。<br><br>書類の書き方から企業ごとの面接対策まで細かくサポートしてもらい、短期間で営業職の内定を獲得できました。収入も安定し、家族にも安心してもらえています。一人で悩まず相談して本当によかったです。</p>
  </article>
</section>

<section class="apply">
  <div class="apply-box">
    <h2 class="apply-head">無料カウンセリングの申し込みはこちら</h2>
    <p class="apply-intro">下記の申し込みフォームにご入力の上「上記に同意して応募する」ボタンを押してください。<br>担当者より改めてご連絡いたします。カウンセリングのお日程はご相談の上で決定いたします。すべて無料でご利用いただけます。</p>
    <div class="form-table">
      <div class="row"><div class="row-label">お名前<span class="req">必須</span></div><div class="row-field"><div class="input" style="width:220px"></div><div class="input" style="width:220px"></div></div></div>
      <div class="row"><div class="row-label">ふりがな<span class="req">必須</span></div><div class="row-field"><div class="input" style="width:220px"></div><div class="input" style="width:220px"></div></div></div>
      <div class="row"><div class="row-label">性別<span class="req">必須</span></div><div class="row-field"><span class="radio"><i class="on"></i>男性</span><span class="radio"><i></i>女性</span></div></div>
      <div class="row"><div class="row-label">誕生年<span class="req">必須</span></div><div class="row-field"><span>西暦</span><div class="input" style="width:140px"></div><span>年</span></div></div>
      <div class="row"><div class="row-label">お住まい<span class="req">必須</span></div><div class="row-field"><div class="select">東京都 ▾</div></div></div>
      <div class="row"><div class="row-label">お電話番号(携帯可)<span class="req">必須</span></div><div class="row-field"><div class="input" style="width:300px"></div></div></div>
      <div class="row"><div class="row-label">メールアドレス<span class="req">必須</span></div><div class="row-field" style="flex-direction:column;align-items:flex-start;justify-content:center;gap:6px"><div class="input" style="width:420px"></div><span style="font-size:12px">※メール受信設定をされている方は「@mosuplint.jp」のドメイン受信を許可してください。</span></div></div>
      <div class="row tall"><div class="row-label">ご要望など</div><div class="row-field"><div class="input" style="width:100%;height:120px"></div></div></div>
    </div>
    <div class="agree">こちらをご確認ください ⇒ <a>「個人情報の取り扱い」</a><p>※上記「個人情報の取り扱い」に関する事項にご同意の上で、ご応募ください。</p></div>
    <div class="submit">上記に同意して応募する ▶</div>
  </div>
</section>

<section class="access">
  <h2 class="access-title">アクセスマップ</h2>
  <p class="access-text">モスプリントの就職カウンセリングは以下2拠点にて実施しております。<br>いずれも駅から5分以内のアクセスが大変便利な場所にございます。お仕事帰りや授業の合間にもお気軽にお立ち寄りください。</p>
  <div class="office main">
    <p class="office-name">本社(渋谷ミナモタワー)</p>
    <div class="office-photo" role="img" aria-label="本社が入る高層ビルの写真"></div>
    <p class="office-addr">〒150-0000<br>東京都渋谷区緑町4-8-2 渋谷ミナモタワー 17F</p>
  </div>
  <div class="office branch">
    <p class="office-name">立川支店</p>
    <div class="office-photo" role="img" aria-label="立川支店が入るビルの写真"></div>
    <p class="office-addr">〒190-0000<br>東京都立川市若葉台2-5-9 立川サクラビル 6F</p>
  </div>
  <div class="pagetop">ページ上部へ ▲</div>
</section>

<footer class="foot">
  <div class="foot-badge"></div>
  <p class="copy">© 2014 Mosuplint Co., Ltd.</p>
</footer>

</body>
</html>
```